Tallow Crest Business Card

We need a business card designed for a a company called "Tallow Crest". We offer consulting, coaching and training to business leaders and coaches (across the world) using the latest findings in neuroscience, social and emotional intelligence and positive psychology. The final design should communicate the use of brain science to create sustainable relationships.

The card should be doublesided. The logo is attached and names and titles will be provided to the successful designer. Thank you.

Industry/Entity Type

Training

```html
<!DOCTYPE html>
<html lang="en">
<head>
<meta charset="utf-8">
<title>Tallow Crest Business Card</title>
<link rel="stylesheet" href="https://fonts.googleapis.com/css2?family=Roboto+Slab:wght@400;700&display=swap">
<style>
  :root {
    --page: #ffffff;
    --tile-edge: #0f0f16;
    --tile-mid: #1b1a24;
    --tile-inner: #2a2836;
    --tile-glow: #3a3848;
    --mark-bg: #050507;
    --brand-blue: #1f8fd0;
    --back-navy: #191d28;
    --strip-light: #e6e6e6;
    --strip-shade: #bdbdbd;
    --panel-white: #ffffff;
    --panel-shade: #d4d4d4;
    --crowd: #0c0f16;
    --ink: #1a1a1a;
  }
  * { box-sizing: border-box; margin: 0; padding: 0; }
  html, body { width: 901px; height: 1200px; overflow: hidden; background: var(--page); }
  body { position: relative; font-family: "Roboto Slab", Georgia, serif; }

  .card {
    position: absolute;
    left: 170px;
    width: 560px;
    height: 320px;
    overflow: hidden;
  }
  .card--front { top: 140px; background: var(--tile-edge); }
  .card--back { top: 720px; background: var(--back-navy); }

  /* front: grid of soft tiles */
  .tile-grid {
    position: absolute; inset: 0;
    display: grid;
    grid-template-columns: repeat(5, 1fr);
    grid-template-rows: repeat(3, 1fr);
  }
  .tile { background: var(--tile-edge); }
  .tile--mid { background: radial-gradient(circle at 50% 50%, var(--tile-mid), var(--tile-edge)); }
  .tile--inner { background: radial-gradient(circle at 50% 50%, var(--tile-glow), var(--tile-inner)); }
  .tile--center { background: var(--mark-bg); display: flex; flex-direction: column; align-items: center; justify-content: center; gap: 8px; }
  .brand-square { width: 22px; height: 22px; background: var(--brand-blue); }
  .brand-name {
    font-weight: 700; font-size: 14px; color: var(--brand-blue);
    text-align: center; line-height: 1.1;
  }

  /* back */
  .brand-strip {
    position: absolute; left: 77px; top: 0;
    width: 98px; height: 212px;
    background: linear-gradient(90deg, var(--strip-shade), var(--strip-light) 35%, var(--strip-light) 65%, var(--strip-shade));
    display: flex; flex-direction: column; align-items: center; justify-content: flex-end;
    padding-bottom: 18px; gap: 10px;
  }
  .brand-strip .brand-square { background: var(--ink); width: 30px; height: 30px; }
  .brand-strip .brand-name { color: var(--ink); font-size: 13px; }

  .crowd-band {
    position: absolute; left: 182px; top: 88px;
    width: 308px; height: 35px;
    background: linear-gradient(180deg, var(--back-navy), var(--crowd));
  }
  .info-panel {
    position: absolute; left: 182px; top: 123px;
    width: 308px; height: 197px;
    background: radial-gradient(ellipse at 50% 45%, var(--panel-white) 55%, var(--panel-shade));
    padding: 18px 14px;
    color: var(--ink);
    font-size: 14.5px; line-height: 1.3;
  }
  .info-panel .contact { margin-bottom: 20px; }
</style>
</head>
<body>
  <section class="card card--front" aria-label="Card front">
    <div class="tile-grid">
      <div class="tile"></div><div class="tile tile--mid"></div><div class="tile tile--mid"></div><div class="tile tile--mid"></div><div class="tile"></div>
      <div class="tile tile--mid"></div><div class="tile tile--inner"></div>
      <div class="tile tile--center">
        <span class="brand-square"></span>
        <span class="brand-name">Tallow Crest</span>
      </div>
      <div class="tile tile--inner"></div><div class="tile tile--mid"></div>
      <div class="tile"></div><div class="tile tile--mid"></div><div class="tile tile--mid"></div><div class="tile tile--mid"></div><div class="tile"></div>
    </div>
  </section>

  <section class="card card--back" aria-label="Card back">
    <div class="brand-strip">
      <span class="brand-square"></span>
      <span class="brand-name">Tallow Crest</span>
    </div>
    <div class="crowd-band" role="img" aria-label="Row of small standing figure silhouettes"></div>
    <div class="info-panel">
      <p class="contact">Dr. Owen Harlow<br>555 0142 3386</p>
      <p>Your personal information here<br>It's an example.</p>
    </div>
  </section>
</body>
</html>
```